Hemp oil , Manuka and botanicals skin care and Castile-liquid soap

I need a design that looks organic colourful and depicts the raw ingredients
I make a range of skin care products and Castile soap with hemp seed oil as a major ingredient
I am a life long farmer and love medicinal plants.
I need a design that will fit on glass jars and tall bottles.
This is a passion for me. I use all of my own products.
Name. “Fallow Crest”
I love the idea of sketches in a botanical style

Target Market(s)

Mid 20 year olds to 60

Industry/Entity Type

Health And Wellness

Font styles to use
Script
Other font styles liked:
• uchronia

```html
<!DOCTYPE html>
<html lang="en">
<head>
<meta charset="utf-8">
<title>Fallow Crest — Castile Liquid Soap</title>
<link rel="stylesheet" href="https://fonts.googleapis.com/css2?family=Cormorant+Garamond:wght@500&family=Cormorant+SC:wght@500&family=Great+Vibes&display=swap">
<style>
  :root {
    --kraft: #c9b18e;
    --ink: #17140f;
    --sage: #6f8a6b;
    --sage-line: #7f9678;
    --leaf-dark: #3e4339;
    --blossom: #c9a9c8;
  }
  html, body {
    margin: 0;
    padding: 0;
    overflow: hidden;
    background: var(--kraft);
  }
  .label {
    position: relative;
    width: 1200px;
    height: 1200px;
    background: var(--kraft);
    overflow: hidden;
  }
  .brand-name {
    position: absolute;
    left: 0;
    top: 0;
    margin: 0;
    font-family: "Cormorant Garamond", "Times New Roman", serif;
    font-weight: 500;
    font-size: 106px;
    line-height: 1;
    color: var(--ink);
    text-transform: uppercase;
    letter-spacing: -1px;
  }
  .brand-name .line {
    position: absolute;
    white-space: nowrap;
  }
  .brand-name .line-first { left: 443px; top: 160px; }
  .brand-name .line-second { left: 469px; top: 250px; }
  .divider {
    position: absolute;
    left: 131px;
    top: 368px;
    width: 935px;
    height: 8px;
  }
  .product-name {
    position: absolute;
    left: 0;
    width: 1200px;
    top: 405px;
    margin: 0;
    text-align: center;
    font-family: "Great Vibes", cursive;
    font-weight: 400;
    font-size: 112px;
    line-height: 1.2;
    color: var(--ink);
  }
  .ingredients {
    position: absolute;
    left: 0;
    width: 1200px;
    top: 570px;
    margin: 0;
    text-align: center;
    font-family: "Cormorant SC", "Times New Roman", serif;
    font-weight: 500;
    font-size: 34px;
    letter-spacing: 0.5px;
    color: var(--sage);
  }
  .botanical-illustration {
    position: absolute;
    left: 431px;
    top: 643px;
    width: 346px;
    height: 480px;
    border-radius: 40% 40% 30% 30% / 30% 30% 25% 25%;
    background: linear-gradient(180deg, var(--leaf-dark) 0%, #5a5c52 55%, var(--blossom) 85%, #b9a6b5 100%);
    opacity: 0.85;
  }
</style>
</head>
<body>
  <main class="label">
    <h1 class="brand-name">
      <span class="line line-first">Fallow</span>
      <span class="line line-second">Crest</span>
    </h1>

    <svg class="divider" viewBox="0 0 935 8" preserveAspectRatio="none" aria-hidden="true">
      <polygon points="0,4 467,1.5 935,4 467,6.5" fill="var(--sage-line)"/>
    </svg>

    <h2 class="product-name">Castile liquid soap</h2>
    <p class="ingredients">With hemp and manuka oil</p>

    <div class="botanical-illustration" role="img" aria-label="Botanical sketch of a hemp plant with manuka blossoms at its base"></div>
  </main>
</body>
</html>
```